Tavern Wren Benefit COncert

I need a concert poster designed that I can send ready to go to one of the sites (e.g. print pad pro). The Pertinent information is

What: Tavern Wren Benefit Concert
Who: Lorne & The Iron Mule Rangers Featuring Dale Pruwitt
Special Guests Curtis, Tessa Varnick
Master of Ceremonies Corinne Walsh
Stand Up Comedy by The Gilded Kettle's Laugh Brigade

When July 27, doors open at 7 PM
Where: Tavern Wren 4817 Pellman Ave Redwood City

Proceeds benefit The Harbor Lodge which is dedicated to serving the families of our wounded soldiers

Sponsors
Tavern Wren, The Ridgeway Savings Cooperative, and Kestrel Medical

Reason: Everett, I'm off the grid on a trip, hard to get wifi...when i am back if you update the stage name for Curtis, we are good... LOrne

• I have to verify how curtis wants to be named. You can pull images from
www.Dalepruwitt.example
www.tessavarnick.example,
www.ridgewaysavingscoop.example/
www.tavernwrenvenue.example
www.harborlodgecare.example
http://www.videohub.example/user/Lornethecoffeebrewer

https://www.gildedkettlelaughs.example/

```html
<!DOCTYPE html>
<html lang="en">
<head>
<meta charset="utf-8">
<title>Tavern Wren Benefit Concert</title>
<link href="https://fonts.googleapis.com/css2?family=Alfa+Slab+One&family=Arvo:wght@700&display=swap" rel="stylesheet">
<style>
  :root {
    --lime: #b0d600;
    --teal: #3bb4c4;
    --navy: #2b1c6b;
    --white: #ffffff;
    --ink: #1e1a2e;
    --photo-dark: #3a3a3a;
    --photo-warm: #b89a7a;
  }
  html, body { margin: 0; padding: 0; overflow: hidden; }
  .poster {
    position: relative;
    width: 1200px;
    height: 1000px;
    overflow: hidden;
    font-family: "Arvo", "Rockwell", serif;
  }
  .backdrop {
    position: absolute; inset: 0;
    background: linear-gradient(100deg, var(--lime) 0%, var(--lime) 36%, var(--teal) 52%, var(--teal) 100%);
  }
  .beneficiary {
    position: absolute; left: 118px; top: 33px;
    width: 224px; height: 224px; border-radius: 50%;
    background: var(--navy);
    display: flex; align-items: center; justify-content: center;
    text-align: center;
    color: var(--white);
    font-size: 28px; line-height: 1.2;
  }
  .title {
    position: absolute; left: 600px; top: 30px; width: 600px;
    margin: 0; text-align: center;
    font-family: "Alfa Slab One", "Rockwell", serif; font-weight: 400;
    color: var(--navy); font-size: 50px; line-height: 58px;
  }
  .label {
    position: absolute; margin: 0;
    font-family: "Alfa Slab One", "Rockwell", serif; font-weight: 400;
    color: var(--navy); font-size: 58px; line-height: 1;
  }
  .label-who { left: 453px; top: 342px; }
  .label-when { left: 404px; top: 712px; }
  .label-where { left: 196px; top: 792px; }
  .lineup {
    position: absolute; left: 560px; top: 250px; width: 620px;
    text-align: center; color: var(--white);
    font-size: 28px; line-height: 39.5px;
  }
  .lineup p { margin: 0; }
  .detail {
    position: absolute; margin: 0; color: var(--white); font-size: 28px;
  }
  .detail-when { left: 618px; top: 722px; }
  .detail-where { left: 432px; top: 805px; }
  .photo {
    position: absolute; border-radius: 50%;
  }
  .photo-guitarist {
    left: 35px; top: 440px; width: 210px; height: 210px;
    background: radial-gradient(circle at 45% 40%, #8a8a8a, var(--photo-dark) 70%);
  }
  .photo-singer {
    left: 262px; top: 423px; width: 246px; height: 246px;
    background: radial-gradient(circle at 45% 40%, var(--photo-warm), #4a4a40 75%);
  }
  .sponsors-label {
    position: absolute; left: 530px; top: 922px; margin: 0;
    color: var(--ink); font-size: 17px;
  }
  .sponsor {
    position: absolute; background: var(--white);
    display: flex; align-items: center; justify-content: center; text-align: center;
    color: var(--navy); font-size: 15px; line-height: 1.15;
  }
  .sponsor-venue { left: 672px; top: 878px; width: 80px; height: 90px; }
  .sponsor-bank { left: 770px; top: 893px; width: 150px; height: 70px; }
  .sponsor-medical {
    position: absolute; left: 945px; top: 897px; margin: 0;
    color: var(--ink); font-size: 21px; line-height: 32px; text-align: center;
  }
</style>
</head>
<body>
<main class="poster">
  <div class="backdrop" role="img" aria-label="Lime green and teal paint splatter background"></div>

  <div class="beneficiary">The Harbor<br>Lodge</div>

  <h1 class="title">TAVERN WREN<br>BENEFIT CONCERT</h1>

  <h2 class="label label-who">Who:</h2>
  <div class="lineup">
    <p>Lorne &amp; The Iron Mule Rangers</p>
    <p>Featuring Dale Pruwitt</p>
    <p>Special Guests</p>
    <p>Curtis, Tessa Varnick</p>
    <p>Master of Ceremonies</p>
    <p>Corinne Walsh</p>
    <p>Stand Up Comedy by</p>
    <p>The Gilded Kettle's</p>
    <p>Laugh Brigade</p>
  </div>

  <div class="photo photo-guitarist" role="img" aria-label="Black and white portrait of guitarist Dale Pruwitt"></div>
  <div class="photo photo-singer" role="img" aria-label="Photo of singer Tessa Varnick at a microphone"></div>

  <h2 class="label label-when">When:</h2>
  <p class="detail detail-when">July 27, doors open at 7 PM</p>

  <h2 class="label label-where">Where:</h2>
  <p class="detail detail-where">Tavern Wren 4817 Pellman Ave Redwood City</p>

  <p class="sponsors-label">Sponsors</p>
  <div class="sponsor sponsor-venue">Tavern<br>Wren</div>
  <div class="sponsor sponsor-bank">Ridgeway Savings<br>Cooperative</div>
  <p class="sponsor-medical">Kestrel<br>Medical</p>
</main>
</body>
</html>
```